Bref créative
Environmental Company Bus Card
Kestrel Ecological Bus Card
Professional
Derek Malloy
Director of Operations
418 Fenwick Park Rd Suite B
Calder Point, MD 21999
derek@kestrelecological.com
www.kestrelecological.com
I would like a fairly standard, but flashy/eye catching business card, with the logo and business name on the back of the card.
The card must have the required printing "bleed" around all edges. This wasn't done on the last project.
The logo shows the business name underneath of it. It does not have to be this way. The triangle logo can be the important feature, while the business name can be moved around wherever it is best suited.
Here is the logo file.
Here is the brochure file to see our color scheme and current design choice.

```html
<!DOCTYPE html>
<html lang="en">
<head>
<meta charset="utf-8">
<title>Kestrel Ecological – Business Cards</title>
<link href="https://fonts.googleapis.com/css2?family=Tinos:wght@400;700&family=Arimo:wght@400&display=swap" rel="stylesheet">
<style>
  :root {
    --backdrop: #e4e4e4;
    --paper: #ffffff;
    --ink: #1c1c1c;
    --ink-soft: #555555;
    --night: #0b0b0c;
    --brand-blue: #2f7fc4;
    --brand-sky: #5ab2e6;
    --brand-pale: #b9def3;
    --mist: #d4d8dc;
  }
  * { box-sizing: border-box; margin: 0; padding: 0; }
  html, body { width: 1200px; height: 492px; overflow: hidden; background: var(--backdrop); }
  .sheet { position: relative; width: 1200px; height: 492px; }
  .card {
    position: absolute; width: 380px; height: 216px; overflow: hidden;
    box-shadow: 0 3px 10px rgba(0,0,0,.25);
    font-family: "Tinos", "Times New Roman", serif;
  }
  .card--light { background: var(--paper); color: var(--ink); }
  .card--dark { background: var(--night); color: #fff; }
  .card--sky { background: radial-gradient(circle at 50% 45%, var(--brand-pale), var(--brand-sky) 75%); color: #fff; }
  .front-white { left: 205px; top: 14px; }
  .front-black { left: 615px; top: 14px; }
  .back-white { left: 12px; top: 262px; }
  .back-black { left: 410px; top: 262px; }
  .back-sky { left: 808px; top: 262px; }

  .swoosh { position: absolute; inset: 0; }
  .front-mark { position: absolute; left: 26px; top: 26px; width: 24px; height: 24px; border-radius: 50%; background: var(--brand-blue); }
  .company { position: absolute; left: 60px; top: 26px; font-size: 21px; font-weight: 400; white-space: nowrap; }
  .contact { position: absolute; left: 208px; top: 92px; font-family: "Arimo", Arial, sans-serif; font-size: 8.5px; line-height: 1.35; }
  .contact .name { font-size: 11px; }
  .contact .title { margin-bottom: 5px; color: var(--ink-soft); }
  .card--dark .contact .title { color: #bbb; }
  .contact .label { display: inline-block; width: 10px; color: var(--brand-blue); }
  .contact .address { margin-top: 6px; }

  .back-center { position: absolute; left: 0; right: 0; top: 50px; text-align: center; }
  .back-mark { display: block; margin: 0 auto 10px; width: 64px; height: 64px; border-radius: 50%; background: var(--brand-blue); }
  .card--dark .back-mark, .card--sky .back-mark { background: var(--mist); }
  .back-name { font-size: 22px; font-weight: 400; white-space: nowrap; }
  .web { position: absolute; left: 0; right: 0; bottom: 16px; text-align: center; font-size: 8px; letter-spacing: 1px; }
</style>
</head>
<body>
<div class="sheet">

  <section class="card card--light front-white">
    <svg class="swoosh" viewBox="0 0 380 216" aria-hidden="true">
      <path d="M150 0 C40 60 10 140 30 216" fill="none" stroke="var(--brand-blue)" stroke-width="3"/>
      <path d="M168 0 C70 70 40 150 58 216" fill="none" stroke="var(--mist)" stroke-width="1.5"/>
    </svg>
    <span class="front-mark"></span>
    <h1 class="company">Kestrel Ecological, LLC</h1>
    <div class="contact">
      <div class="name">Derek Malloy</div>
      <div class="title">Director of Operations</div>
      <div><span class="label">p</span>410-555-0182</div>
      <div><span class="label">c</span>443-555-0147</div>
      <div><span class="label">f</span>410-555-0139</div>
      <div><span class="label">e</span>derek@kestrelecological.com</div>
      <div><span class="label">w</span>www.kestrelecological.com</div>
      <div class="address">418 Fenwick Park Rd Suite B<br>Calder Point, MD 21999</div>
    </div>
  </section>

  <section class="card card--dark front-black">
    <svg class="swoosh" viewBox="0 0 380 216" aria-hidden="true">
      <path d="M150 0 C40 60 10 140 30 216" fill="none" stroke="var(--brand-sky)" stroke-width="3"/>
      <path d="M168 0 C70 70 40 150 58 216" fill="none" stroke="#444" stroke-width="1.5"/>
    </svg>
    <span class="front-mark"></span>
    <h1 class="company">Kestrel Ecological, LLC</h1>
    <div class="contact">
      <div class="name">Derek Malloy</div>
      <div class="title">Director of Operations</div>
      <div><span class="label">p</span>410-555-0182</div>
      <div><span class="label">c</span>443-555-0147</div>
      <div><span class="label">f</span>410-555-0139</div>
      <div><span class="label">e</span>derek@kestrelecological.com</div>
      <div><span class="label">w</span>www.kestrelecological.com</div>
      <div class="address">418 Fenwick Park Rd Suite B<br>Calder Point, MD 21999</div>
    </div>
  </section>

  <section class="card card--light back-white">
    <div class="back-center">
      <span class="back-mark"></span>
      <h2 class="back-name">Kestrel Ecological, LLC</h2>
    </div>
    <p class="web">WWW.KESTRELECOLOGICAL.COM</p>
  </section>

  <section class="card card--dark back-black">
    <div class="back-center">
      <span class="back-mark"></span>
      <h2 class="back-name">Kestrel Ecological</h2>
    </div>
    <p class="web">WWW.KESTRELECOLOGICAL.COM</p>
  </section>

  <section class="card card--sky back-sky">
    <div class="back-center">
      <span class="back-mark"></span>
      <h2 class="back-name">Kestrel Ecological</h2>
    </div>
    <p class="web">WWW.KESTRELECOLOGICAL.COM</p>
  </section>

</div>
</body>
</html>
```